High School Senior Ad for annual

My son is a senior, and we bought an Ad for the back of the annual and looking for a one page Ad that meets the below specification. We have to submit out final Ad by Monday 11/07/22.

Specifications:
- Must be a JPEG @ 300 DPI.
- Full page size is 8.667 inches wide by 11.333 inches tall, or 2600 pixels by 3400 pixels.
- Do NOT take wording to the edge. Leave at least ½ inch on all sides without wording.

What we want:
- Looking for a creative artistic use of the photo we provide
- His name Tobin Garrick should be in a very artistic script at the top
- Insert the attached bible verse and text somewhere on the Ad
- I'm attaching some examples of some that we like along with the photos that we want to use. Please look at the instruction doc to understand what we are looking for.
- If you have questions, please ask

```html
<!DOCTYPE html>
<html lang="en">
<head>
<meta charset="utf-8">
<title>Tobin Garrick – Senior Ad</title>
<link rel="stylesheet" href="https://fonts.googleapis.com/css2?family=Allison&family=Montserrat:wght@400;500;900&family=Poppins:wght@400;700&display=swap">
<style>
  :root {
    --backdrop: #f6f4ee;
    --photo-dark: #1f2a3a;
    --photo-mid: #4a5566;
    --photo-light: #9aa3ad;
    --film: #ffffff;
    --film-hole: #1c2430;
    --panel: rgba(28, 30, 36, 0.72);
    --ink-light: #ffffff;
    --pill: #f0dc82;
    --ink-dark: #1a1a1a;
  }
  * { margin: 0; padding: 0; box-sizing: border-box; }
  html, body { width: 1200px; height: 912px; overflow: hidden; }
  body { background: var(--backdrop); position: relative; }

  .ad-page {
    position: absolute; left: 271px; top: 26px;
    width: 658px; height: 860px; overflow: hidden;
    box-shadow: 0 6px 18px rgba(0,0,0,0.35);
  }
  .hero-photo {
    position: absolute; inset: 0;
    background:
      linear-gradient(90deg, rgba(138,74,60,0.35) 0%, transparent 18%, transparent 85%, rgba(138,74,60,0.35) 100%),
      linear-gradient(180deg, var(--photo-mid) 0%, var(--photo-dark) 45%, var(--photo-dark) 70%, var(--photo-light) 100%);
  }

  .name-script {
    position: absolute; left: 104px; top: 180px;
    font-family: "Allison", cursive; font-size: 200px; line-height: 1;
    color: var(--ink-light); z-index: 3;
  }
  .name-block {
    position: absolute; left: 150px; top: 338px; width: 320px;
    font-family: "Montserrat", sans-serif; font-weight: 900; font-size: 60px;
    line-height: 1; letter-spacing: -1px; color: var(--ink-light);
    text-align: right; z-index: 2;
  }
  .verse-pill {
    position: absolute; left: 163px; top: 406px; width: 306px; height: 38px;
    background: var(--pill); border-radius: 19px;
    font-family: "Poppins", sans-serif; font-weight: 700; font-size: 11.5px;
    line-height: 1.3; color: var(--ink-dark); text-align: center;
    display: flex; flex-direction: column; justify-content: center;
    z-index: 4;
  }

  .message-panel {
    position: absolute; left: 47px; width: 422px;
    background: var(--panel); color: var(--ink-light);
  }
  .message-parents {
    top: 463px; height: 285px; padding: 14px 10px 10px 12px;
    font-family: "Montserrat", sans-serif; font-weight: 500;
    font-size: 11.9px; line-height: 15.2px; letter-spacing: 0.6px;
  }
  .message-sibling {
    top: 757px; height: 81px; padding: 11px 30px 10px 19px;
    font-family: "Poppins", sans-serif; font-weight: 400;
    font-size: 11.8px; line-height: 15px;
  }

  .film-strip { position: absolute; left: 486px; top: 88px; width: 145px; height: 712px; }
  .film-photo { position: absolute; left: 20px; width: 104px; }
  .film-photo--kid { top: 4px; height: 169px; background: linear-gradient(180deg, #b99a4c, #3f8a4a); }
  .film-photo--golf { top: 184px; height: 168px; background: linear-gradient(180deg, #7c8a6a, #4f7a3a); }
  .film-photo--wall { top: 359px; height: 169px; background: linear-gradient(180deg, #b86a62, #8d8a8c); }
  .film-photo--steps { top: 539px; height: 167px; background: linear-gradient(180deg, #8b6a5a, #c9c2b4); }
</style>
</head>
<body>
  <main class="ad-page">
    <div class="hero-photo" role="img" aria-label="Senior portrait of the graduate in a navy blazer and striped tie, seated by an iron gate"></div>

    <div class="name-script">Tobin</div>
    <div class="name-block">GARRICK</div>
    <div class="verse-pill"><span>Behold, children are a gift from the Lord....</span><span>Psalm 127:3</span></div>

    <section class="message-panel message-parents">
      Tobin, you are a blessing from the Lord, and we are so thankful for you. You have brought so much joy and love into our lives. It has been an honor to watch you grow into an amazing, kind, intelligent, and hard-working young man. We have loved every minute of watching you play golf for RCA. Your strong work ethic during golf season was inspiring. We are so proud of you, and we are excited to see the wonderful plans God has for your life. We will always be here to love, support, and encourage you. We hope you never outgrow your love of travel, history, and a good book!<br>
      Remember, “The more that you read, the more things that you will know. The more that you learn, the more places you’ll go!” –<br>
      Dr. Pemberton<br>
      Love,<br>
      Mom &amp; Dad
    </section>

    <section class="message-panel message-sibling">
      Tobin, Congrats on graduating! I hope you enjoyed your senior year as much as I did. Good luck at Harlow University; you’ll do great!<br>
      Love, Caleb
    </section>

    <div class="film-strip">
      <svg width="145" height="712" viewBox="0 0 145 712" aria-hidden="true">
        <defs>
          <pattern id="sprockets" width="145" height="14" patternUnits="userSpaceOnUse">
            <rect x="5" y="4" width="8" height="7" rx="1.5" fill="var(--film-hole)"/>
            <rect x="132" y="4" width="8" height="7" rx="1.5" fill="var(--film-hole)"/>
          </pattern>
        </defs>
        <rect x="0" y="0" width="145" height="712" fill="var(--film)"/>
        <rect x="0" y="0" width="145" height="712" fill="url(#sprockets)"/>
      </svg>
      <div class="film-photo film-photo--kid" role="img" aria-label="Childhood photo holding a soccer ball in a green jersey"></div>
      <div class="film-photo film-photo--golf" role="img" aria-label="Carrying a golf bag across a green course"></div>
      <div class="film-photo film-photo--wall" role="img" aria-label="Standing by a car in front of a painted mural wall"></div>
      <div class="film-photo film-photo--steps" role="img" aria-label="Seated on outdoor steps in a dress shirt and khakis"></div>
    </div>
  </main>
</body>
</html>
```